DISCUSSION TOPICS: Launching Miss Jolene’s New e-Commerce Business

A native PowerPoint presentation outlining topics to be considered by a young teenager in launching her new e-commerce shop, primarily selling clothes and dolls online. The project consists of a title slide and topics grouped into 10 sections plus a closing. (I have uploaded the native Word document for the ease of cutting & pasting.) The design and colors should appeal to a young, aspiring fashionista and entrepreneur. Jolene's overall message in her packages is motivational and very spiritual (religious). Please insert royalty free stock photos or graphics to break up the text, as you deem appropriate. For selection, please submit the cover slide and slides for the first two chapters, designated by number and color in the attached. (This will not be a lengthy presentation.) Each new chapter/number/color should begin on a new slide, and the pages should NOT be numbered, so the facilitator can select chapters at random and present them out of the sequence of the PowerPoint presentation. I also have uploaded my logo and tagline for Dapple on Main. It need not be a central component of the design, but I would like it incorporated in some small way, perhaps on the title page or in the footer of each page, wherever you feel is most appropriate. I paid an expedite fee when I posted the project since, ideally, I would like to distribute the presentation on Friday, July 29. Many thanks for considering this project that is urgently anticipated by the young recipient.
Updates
Thank you for viewing my invitation to work on my DISCUSSION TOPICS project. Especially since the recipient will be a young girl, expediency is of a higher priority than corporate perfection. Of course, I am depending upon you for a lively, creative design so Jolene will enjoy looking at your slides while the facilitator walks her through the content. Ideally, I would like to send the presentation to the facilitator on Friday, July 29. (For time zone reference, I reside in Texas.) I do not require three separate designs as advertised on the ArtFlock site. I would prefer to work with you on only one that you consider a very appropriate, good design rather than stretching your time too thin for the ideal delivery window by forcing alternate designs. Many thanks! Please feel very welcome to contact me with any questions or requests for clarification. -- Greta

Target Market(s)
Teenagers for sales and the infirm for motivational and spiritual gifts
Industry/Entity Type
Seller on e-commerce sites like Tradelo and Vendora
Colors
Designer to choose colors to be used in the design.
Requirements
Must have
- A bold, modern, creative yet simple design that will appeal to a young female recipient.

Nice to have
- Graphics and royalty-free photos to break up the monotony of the dense text

Should not have
- Do not number the pages so "chapters" can be pulled and presented out of sequence

```html
<!DOCTYPE html>
<html lang="en">
<head>
<meta charset="utf-8">
<title>Dapple on Main – Discussion Topics</title>
<link href="https://fonts.googleapis.com/css2?family=Poppins:wght@400;500;600;700&family=Sansita+Swashed:wght@400&display=swap" rel="stylesheet">
<style>
:root{
  --berry:#9a3a6a;
  --berry-deep:#7e2a55;
  --berry-soft:#c06a9b;
  --blush:#f3e4ec;
  --ink:#1f1a1d;
  --paper:#ffffff;
  --canvas:#ececec;
  --photo-warm:#d9c4b8;
  --photo-dark:#3b2c29;
}
*{box-sizing:border-box;margin:0;padding:0}
html,body{width:1200px;height:4231px;overflow:hidden;background:var(--canvas)}
body{font-family:"Poppins",sans-serif;color:var(--ink);position:relative}
.slide{position:absolute;left:61px;width:1078px;height:606px;overflow:hidden;box-shadow:0 4px 10px rgba(0,0,0,.18);background:var(--paper)}
.script{font-family:"Sansita Swashed",cursive;font-weight:400}
.abs{position:absolute}
.footer-tag{position:absolute;right:16px;bottom:14px;font-size:18px;color:var(--berry)}
.mini-brand{position:absolute;right:16px;top:18px;font-size:10px;color:var(--berry);display:flex;align-items:center;gap:4px}
.mini-brand i{width:6px;height:6px;border-radius:50%;background:var(--berry-soft);display:inline-block}

/* cover */
.cover{top:85px;background:linear-gradient(180deg,#94406d,#a0507b 60%,#8e3a67)}
.cover .title{top:112px;width:100%;text-align:center;color:#fff;font-size:50px}
.cover .tagline{top:410px;width:100%;text-align:center;color:#fff;font-size:40px}
.cover .dots{top:506px;left:0;width:100%;display:flex;justify-content:center;gap:8px}
.cover .dots span{width:32px;height:32px;border:1.5px solid #fff;border-radius:50%}
.floral{position:absolute;background:linear-gradient(160deg,rgba(255,255,255,.22),rgba(255,255,255,.05))}

/* who are you */
.who{top:762px}
.who h2{position:absolute;left:553px;top:62px;font-size:28px;font-weight:700}
.who ul{position:absolute;left:553px;top:134px;width:462px;list-style:none}
.who li{position:relative;padding-left:56px;font-size:13px;line-height:25px;margin-bottom:17px}
.who li::before{content:"";position:absolute;left:0;top:8px;width:34px;height:7px;border-bottom:2px solid var(--berry-soft);border-radius:0 0 40px 10px}
.who .note{font-size:9.5px;line-height:17px;margin:-12px 0 17px;padding-left:72px;position:relative}
.who .note::before{content:"";position:absolute;left:56px;top:5px;width:6px;height:6px;border-radius:50%;background:var(--berry-soft)}

/* customers */
.customers{top:1448px;background:linear-gradient(90deg,#b05a8a,#9d4475)}
.customers .copy{position:absolute;left:0;width:100%;text-align:center;color:#fff}
.customers h2{top:40px;font-size:26px;font-weight:600;line-height:42px}
.customers .qs{top:158px;font-size:13px;line-height:34px}
.customers .qs small{display:block;font-size:9.5px;line-height:20px}
.customers .brand{position:absolute;left:60px;bottom:44px;color:#fff;font-size:11px;display:flex;gap:5px;align-items:center}
.customers .brand i{width:7px;height:7px;border-radius:50%;background:#fff}
.customers .footer-tag{color:#fff;font-size:22px}

/* personal */
.personal{top:2139px}
.personal .panel{left:0;top:0;width:478px;height:397px;background:linear-gradient(180deg,#a64f80,#b8668f)}
.personal h2{left:60px;top:50px;color:#fff;font-size:31px;font-weight:700;line-height:50px}
.personal .notes{left:522px;top:30px;width:480px}
.personal .notes p{font-size:9.2px;line-height:18.5px;font-weight:500;border-left:2px solid var(--berry);padding-left:14px;margin-bottom:19px}
.personal .notes .sub{border:0;font-size:7.8px;line-height:16px;padding-left:24px;position:relative}
.personal .notes .sub::before{content:"";position:absolute;left:14px;top:6px;width:4px;height:4px;border-radius:50%;background:var(--berry)}

/* brand everything */
.brand-all{top:2843px;background:linear-gradient(180deg,#f7f1f3,#f2eaee)}
.brand-all h2{left:28px;top:48px;font-size:22px;font-weight:700}
.brand-all p{position:absolute;font-size:11px;line-height:22px}
.leaf{position:absolute;border:2px solid var(--berry);border-radius:0 60% 0 60%}

/* thanks */
.thanks{top:3538px;background:linear-gradient(120deg,#e9ddd6,#d8c4b6)}
.thanks .name{left:333px;top:122px;color:#fff;font-size:30px}
.thanks h2{left:299px;top:286px;color:#fff;font-size:36px;font-weight:700}
.thanks ul{position:absolute;left:299px;top:362px;list-style:none;color:#fff;font-size:12px}
.thanks li{display:flex;align-items:flex-start;gap:12px;margin-bottom:20px;width:300px;line-height:16px}
.thanks li svg{flex:none}
</style>
</head>
<body>

<section class="slide cover">
  <div class="abs" role="img" aria-label="Faint city skyline photo behind the title" style="left:150px;top:40px;width:780px;height:540px;background:linear-gradient(180deg,rgba(255,255,255,.04),rgba(60,20,45,.18))"></div>
  <div class="floral" role="img" aria-label="White leafy vine ornament" style="left:0;top:0;width:170px;height:606px;border-radius:0 80% 80% 0"></div>
  <div class="floral" role="img" aria-label="White leafy vine ornament" style="right:0;top:0;width:170px;height:606px;border-radius:80% 0 0 80%"></div>
  <div class="abs script title">Dapple on Main</div>
  <div class="abs script tagline">Fresh Finds with a Flourish</div>
  <div class="abs dots"><span></span><span></span><span></span><span></span></div>
</section>

<section class="slide who">
  <svg class="abs" style="left:0;top:0" width="520" height="606" viewBox="0 0 520 606">
    <path d="M0 0H520C470 230 330 470 150 606H0Z" fill="var(--berry)"/>
    <path d="M0 0H478C440 200 300 440 60 580L0 590Z" fill="var(--berry-soft)"/>
    <path d="M0 0H440C400 200 240 400 0 500Z" fill="var(--photo-warm)" role="img" aria-label="Flat lay of shoes, scarf, ribbon and perfume"/>
  </svg>
  <div class="mini-brand script"><i></i>Dapple on Main</div>
  <h2>Who are you?</h2>
  <ul>
    <li>What about you do you most want to project to your customers?</li>
    <li>What is your mission or top priorities for the business?</li>
    <li>Does the name of your business convey what you want to project about yourself or your mission?</li>
    <li>Is your logo easily identifiable/recognizable and aligned with your business name or mission and your selected color(s)?</li>
    <div class="note">I’m sure your graphic design camp will be very helpful in this area. There also are many online tools to help kickstart the process or enhance an in-process logo.</div>
    <li>Is your tagline brief, memorable, and aligned with your business name or mission?</li>
    <li>How can you differentiate yourself from competitors? What makes shopping with you uniquely pleasant?</li>
  </ul>
  <div class="footer-tag script">Fresh Finds with a Flourish</div>
</section>

<section class="slide customers">
  <svg class="abs" style="left:0;top:0" width="1078" height="606" viewBox="0 0 1078 606">
    <ellipse cx="538" cy="110" rx="455" ry="390" fill="var(--photo-dark)" role="img" aria-label="Woman in a brown outfit in a clothing boutique"/>
  </svg>
  <div class="copy" style="top:40px"><h2>Who are your customers &amp; what<br>do they most want?</h2></div>
  <div class="copy qs">
    Is there a target demographic for your business?<br>
    What is most important to that group of potential customers?<br>
    Does your product meet the expectations of your target customers?
    <small>• If you have significant doubts, what can you change about what you are offering?<br>• If your friends represent your target customer base, what do they think about your product?</small>
    How can you deliver what your target customers most want if it’s intangible?
  </div>
  <div class="brand script"><i></i>Dapple on Main</div>
  <div class="footer-tag script">Fresh Finds with a Flourish</div>
</section>

<section class="slide personal">
  <div class="abs panel" role="img" aria-label="Soft-focus boutique shelves in berry tint"></div>
  <h2 class="abs">Make it Personal –<br>Do the Unexpected<br>and Go the Extra Mile</h2>
  <div class="abs" role="img" aria-label="Woman in a camel blazer at a mirror beside a clothing rack" style="left:62px;top:318px;width:352px;height:288px;background:linear-gradient(135deg,#ece7e4,#b58a67)"></div>
  <div class="abs" role="img" aria-label="Pampas grass and berry sprig" style="left:0;top:390px;width:62px;height:216px;background:linear-gradient(180deg,#f4e9ee,#e4cfda)"></div>
  <div class="mini-brand script"><i></i>Dapple on Main</div>
  <div class="abs notes">
    <p>When photographing an item to be listed for sale, ensure that product looks its best for the photo. (You will see more than your fair share of straight-from-the-dryer, wrinkled t-shirts and other crumpled items on Tradelo.) For garments with wrinkles, use your Grandmother’s steamer on the garment prior to photographing it. The photograph is what potential buyers see first. Make sure it’s a good one!</p>
    <p>If you receive an order online, send a message to the buyer after you’ve packaged and addressed the box so they have acknowledgement from you and know when to expect delivery.</p>
    <p>Always include a Thank You note in your packages. I use a Notecraft notecard, with my logo, tagline, and standard Thank You for Your Purchase text on the front, and a personalized note on the back.</p>
    <p>Always include a Thank You note in your packages. I use a Notecraft notecard, with my logo, tagline, and standard Thank You for Your Purchase text on the front, and a personalized note on the back.</p>
    <p>If you become aware of a personal situation, family crisis or celebratory event through your online dialogue with a buyer, send a follow-up message (online or via snail mail) a few weeks later to inquire about status and to convey your concern, thoughts, prayers, congratulations, or whatever is most appropriate. (Your grandmother is unparalleled when it comes to this!)</p>
    <p style="margin-bottom:8px">Keep a record of your buyers including the date, what was purchased, their address, and anything extra you included in the package, even the Meadow Mist if you elect to use them. You then have the information at your fingertips for follow-up notes, holiday greetings, etc.</p>
    <p class="sub">Instead of retail holiday cards, consider using your blank Notecraft perforated cardstock so you can include your logo and tagline. Remember, Brand Everything!</p>
  </div>
  <div class="footer-tag script">Fresh Finds with a Flourish</div>
</section>

<section class="slide brand-all">
  <div class="abs" role="img" aria-label="Faded background of packing boxes and clothing" style="inset:0;background:linear-gradient(180deg,rgba(230,215,222,.35),rgba(255,255,255,.2))"></div>
  <svg class="abs" style="left:0;top:0" width="1078" height="606" viewBox="0 0 1078 606">
    <path d="M502 0H528L560 606H468Z" fill="var(--berry-soft)"/>
  </svg>
  <h2 class="abs">Brand Everything!</h2>
  <div class="leaf" role="img" aria-label="Handmade doll in a pink dress" style="left:298px;top:42px;width:154px;height:166px;background:linear-gradient(135deg,#e6d2cf,#b78c8a)"></div>
  <div class="leaf" role="img" aria-label="Hat and garments on a clothing rack" style="left:578px;top:238px;width:160px;height:168px;background:linear-gradient(135deg,#efe8e4,#c09a86)"></div>
  <div class="leaf" role="img" aria-label="Child holding a handmade doll" style="left:288px;top:430px;width:154px;height:168px;background:linear-gradient(135deg,#d9b3a2,#b2506f)"></div>
  <p style="left:586px;top:62px;width:330px;text-align:justify">To ensure your brand/logo is what customers first see upon receiving a package from you, I suggest not reusing boxes from online retailers. Those boxes have the retailer’s printed logo, tape, shipping labels, etc. Although it’s economical to repurpose those boxes, it does not provide a “clean” first impression to your customers.</p>
  <p style="left:146px;top:262px;width:312px;text-align:justify;text-align-last:right">You can more economically brand everything by purchasing blank stickers, folded notecards, postcards and whatever else you need, and printing on them your selected border, logo, tagline, text, etc.</p>
  <p style="left:586px;top:488px;width:250px">Typically, the launch phase cannot support the cost of custom boxes and tissue paper with your logo (and tagline), professionally printed cards and stickers, etc.</p>
  <div class="mini-brand script"><i></i>Dapple on Main</div>
  <div class="footer-tag script">Fresh Finds with a Flourish</div>
</section>

<section class="slide thanks">
  <div class="abs" role="img" aria-label="Clothing rack with knitwear beside woven baskets" style="inset:0;background:linear-gradient(120deg,#efe6df,#cdb09c)"></div>
  <svg class="abs" style="left:0;top:0" width="1078" height="606" viewBox="0 0 1078 606">
    <defs><linearGradient id="fade" x1="0" y1="0" x2="1" y2="1"><stop offset="0" stop-color="#8e3463" stop-opacity=".6"/><stop offset="1" stop-color="#b2608d" stop-opacity=".6"/></linearGradient></defs>
    <path d="M0 0H610C590 90 620 200 720 290C860 410 1080 420 1040 540C1020 600 960 606 940 606H0Z" fill="var(--berry)"/>
    <path d="M0 0H610C590 90 620 200 720 290C860 410 1080 420 1040 540C1020 600 960 606 940 606H0Z" fill="url(#fade)"/>
  </svg>
  <div class="abs script name">Dapple on Main</div>
  <h2 class="abs">THANK YOU</h2>
  <ul>
    <li><svg width="14" height="14" viewBox="0 0 24 24"><path fill="#fff" d="M6.6 10.8a15 15 0 006.6 6.6l2.2-2.2a1 1 0 011-.25 11.4 11.4 0 003.6.57 1 1 0 011 1V20a1 1 0 01-1 1A17 17 0 013 4a1 1 0 011-1h3.5a1 1 0 011 1c0 1.25.2 2.45.57 3.57a1 1 0 01-.25 1z"/></svg>+1 (555) 010 0199</li>
    <li><svg width="14" height="14" viewBox="0 0 24 24"><circle cx="12" cy="12" r="10" fill="#fff"/><path d="M2 12h20M12 2c3 3 3 17 0 20M12 2c-3 3-3 17 0 20" stroke="var(--berry)" stroke-width="1.5" fill="none"/></svg>www.dappleonmain.com</li>
    <li><svg width="14" height="14" viewBox="0 0 24 24"><rect x="2" y="5" width="20" height="14" rx="2" fill="#fff"/><path d="M2 6l10 7 10-7" stroke="var(--berry)" stroke-width="1.5" fill="none"/></svg>hello@dappleonmain.com</li>
    <li><svg width="14" height="14" viewBox="0 0 24 24"><path fill="#fff" d="M12 2a7 7 0 00-7 7c0 5 7 13 7 13s7-8 7-13a7 7 0 00-7-7zm0 9.5A2.5 2.5 0 1112 6.5a2.5 2.5 0 010 5z"/></svg>123,Lorem ipsum dolor sit amet, consectetur adipiscing elit</li>
  </ul>
</section>

</body>
</html>
```